依頼詳細
海の家で開催するアコーステックライブのフライヤーです。

カフェやBarなど店舗に配布します。
開催まで日が少ないため早めに提案頂ける方、宜しくお願いします。

さわやか、ナチュラル、上品、20代~30代女性向け、オシャレな感じ

インスタグラム https://www.instagram.com/k72.note/
FB https://www.facebook.com/sunnyreefhut/

インスタやFBを見ていただき、雰囲気やテイストをイメージしていただければ幸いです。写真も必要であれば使ってください。

潮風の言葉に引っ張られず、自由にデザイン頂きたいです。
記載項目
開催概要
タイトル/潮風芸能祭Autumn Gala
日付/2016/09/11(SUN)
時間/OPEN/16:30 START/17:00 END/20:00
会場/海の家Sunny Reef Hut(佐賀県唐津市潮見町海水浴場)
LIVE/dawnrow/KORUE/MINT RIVER with WABELUK
TICKET/前売¥3,000- 当日¥4,000- 1Drink付
予約方法/①開催日 ②氏名 ③人数 ④連絡先電話番号をお伝えください。
連絡先/TEL080-7010-6213 MAIL info@sunnyreefhut.example

アーティスト情報は添付資料参照ください
サイズ
B6
ページ数
両面
希望イメージ
シンプル 複雑
単色 カラフル
暗い 明るい
日常 高級
遊び心 厳粛
未来的 伝統的
女性的 男性的
希望する色
納品ファイル
• 高解像度JPG (.jpg)
• イラストレーター形式 (.ai)
補足説明
■ 選んだ理由

スタッフの皆で協議の結果選定させていただきました。
ありがとうございました。

■ 提案者全員のお礼・コメント

今回ご提案いただきました皆様、どのデザインも良く、自分たちのイメージに沿った提案をいただき、選定に悩みました。
提案いただき本当にありがとうございました!
今後も機会があれば宜しくお願いします

```html
<!DOCTYPE html>
<html lang="ja">
<head>
<meta charset="utf-8">
<title>潮風芸能祭Autumn Gala フライヤー</title>
<link href="https://fonts.googleapis.com/css2?family=Noto+Serif+JP:wght@400;600;700&family=Playfair+Display:wght@400;600&display=swap" rel="stylesheet">
<style>
:root{
  --paper:#ffffff;
  --navy:#101d3a;
  --navy-soft:#1d2c52;
  --white:#ffffff;
  --cream:#f3ead8;
  --trim:#7a7a7a;
  --label:#2d3d66;
}
*{margin:0;padding:0;box-sizing:border-box}
html,body{width:891px;height:1200px;overflow:hidden;background:var(--paper)}
body{position:relative;font-family:"Noto Serif JP",serif;color:var(--white)}
.trim-marks{position:absolute;inset:0}
.flyer{position:absolute;left:66px;top:60px;width:760px;height:1080px;background:var(--navy);overflow:hidden}
.hero{position:absolute;left:0;top:0;width:543px;height:698px;
  background:linear-gradient(180deg,#2f3f63 0%,#7d7f8f 30%,#d9a874 52%,#a8805e 64%,#3a3430 82%,#1f1c1d 100%)}
.side-photo{position:absolute;left:546px;width:214px}
.side-photo.stars{top:0;height:206px;background:linear-gradient(180deg,#0c1530,#2a3a62 70%,#5a4d5a)}
.side-photo.guitar{top:209px;height:160px;background:radial-gradient(circle at 60% 50%,#b07a45,#3a2618 70%)}
.side-photo.meal{top:372px;height:160px;background:radial-gradient(circle at 50% 55%,#e9dccb,#8d6a4e 75%)}
.side-photo.sunset{top:535px;height:163px;background:linear-gradient(180deg,#f0c58a 0%,#d98f56 45%,#6a6f86 60%,#2e3b5a 100%)}
.brand{position:absolute;left:52px;top:62px;font-family:"Playfair Display",serif;font-weight:600;font-size:30px;line-height:1;color:var(--white)}
.intro{position:absolute;left:52px;top:492px;font-size:21px;line-height:1.45;font-weight:600;text-shadow:0 1px 4px rgba(0,0,0,.5)}
.title-ja{position:absolute;left:50px;top:556px;font-size:62px;font-weight:700;letter-spacing:.04em;text-shadow:0 2px 6px rgba(0,0,0,.45)}
.title-en{position:absolute;left:50px;top:628px;font-family:"Playfair Display",serif;font-size:64px;font-weight:400;line-height:1;text-shadow:0 2px 6px rgba(0,0,0,.45)}
.date{position:absolute;left:46px;top:720px}
.date .year{display:block;font-family:"Playfair Display",serif;font-size:30px;line-height:1}
.date .day{font-family:"Playfair Display",serif;font-size:96px;line-height:1}
.date .dow{display:inline-block;width:40px;height:40px;border-radius:50%;background:var(--white);color:var(--navy);font-size:14px;font-weight:700;text-align:center;line-height:40px;vertical-align:12px;margin-left:6px}
.schedule{position:absolute;left:320px;top:726px;font-size:24px;line-height:1.3;font-family:"Playfair Display",serif}
.venue{position:absolute;left:320px;top:796px;font-size:26px;font-weight:600}
.venue small{display:block;font-size:13px;font-weight:400;margin-top:2px}
.details{position:absolute;left:46px;top:880px;width:470px;font-size:15px;line-height:1.35}
.row{display:flex;align-items:flex-start;margin-bottom:12px}
.row .label{flex:0 0 80px;background:var(--white);color:var(--navy);font-size:13px;font-weight:700;text-align:center;padding:1px 0;margin-right:12px}
.map{position:absolute;left:530px;top:870px;width:200px;height:120px;background:linear-gradient(135deg,#f4f4f4,#dfe3ea)}
</style>
</head>
<body>
<svg class="trim-marks" width="891" height="1200" aria-hidden="true">
  <g stroke="var(--trim)" stroke-width="1" fill="none">
    <path d="M66 0V40M0 60H46M825 0V40M845 60H891M66 1200V1160M0 1140H46M825 1200V1160M845 1140H891"/>
    <path d="M445 0V30M0 600H30M891 600H861M445 1200V1170"/>
  </g>
</svg>

<main class="flyer">
  <div class="hero" role="img" aria-label="夕暮れの海辺に建つ海の家のテラス写真"></div>
  <div class="side-photo stars" role="img" aria-label="満天の星空の写真"></div>
  <div class="side-photo guitar" role="img" aria-label="アコースティックギターの写真"></div>
  <div class="side-photo meal" role="img" aria-label="海の家の料理の写真"></div>
  <div class="side-photo sunset" role="img" aria-label="海に沈む夕日の写真"></div>

  <div class="brand">Sunny Reef Hut</div>

  <p class="intro">海の家Sunny Reef Houseで<br>ゆったりまったりアコーステックライブ</p>
  <h1 class="title-ja">潮風芸能祭</h1>
  <p class="title-en">Autumn Gala</p>

  <div class="date">
    <span class="year">2016</span>
    <span class="day">9/11</span><span class="dow">SUN</span>
  </div>
  <div class="schedule">OPEN/16:30　START/17:00<br><span style="padding-left:190px">END/20:00</span></div>
  <div class="venue">at. 海の家Sunny Reef Hut<small>（佐賀県唐津市潮見町海水浴場）</small></div>

  <div class="details">
    <div class="row"><span class="label">LIVE</span><span>dawnrow / KORUE / MINT RIVER with WABELUK</span></div>
    <div class="row"><span class="label">TICKET</span><span>前売¥3,000-　当日¥4,000-　1Drink付</span></div>
    <div class="row"><span class="label">予約方法</span><span>①開催日 ②氏名 ③人数 ④連絡先電話番号をお伝えください。</span></div>
    <div class="row"><span class="label">連絡先</span><span>TEL 090-4825-3917　MAIL info@sunnyreefhut.example</span></div>
  </div>

  <div class="map" role="img" aria-label="会場周辺の案内地図"></div>
</main>
</body>
</html>
```